Tortilla Business needs a design for a shelf talker

We need a design for our retail display and for our stockist's retail display.
Our product is fresh corn tortillas. These can be used to make tacos, quesadillas, tortilla chips and tostadas.
We want the table talker to use our brand style (see our website) and show the tortillas versatility.
lumo-flatbakes.co.uk
It should also have a space for our stockists to write in a blank space under the heading "Our fresh tortillas are delivered every....[blank space]"
The table talker should be 75mm tall x 150mm wide. This will also have a 25mm self adhesive flap at the top which can be blank or the same colour as the background.
Please feel free to use any files from our website as well as illustrations attached.
Target Market(s)
Customers in high end shops and delis
Industry/Entity Type
food and drink

```html
<!DOCTYPE html>
<html lang="en">
<head>
<meta charset="utf-8">
<title>Lumo Flatbakes – Shelf Talker</title>
<link href="https://fonts.googleapis.com/css2?family=League+Spartan:wght@600;800;900&display=swap" rel="stylesheet">
<style>
  :root {
    --navy: #1e2b44;
    --navy-line: #33425e;
    --gold: #e3bd1f;
    --white: #ffffff;
    --backdrop: #e6e6e6;
    --tortilla-light: #efe3c4;
    --tortilla-dark: #c9a86a;
  }
  * { box-sizing: border-box; margin: 0; padding: 0; }
  html, body {
    width: 1200px; height: 672px; overflow: hidden;
    background: var(--backdrop);
    font-family: "League Spartan", "Arial Black", sans-serif;
  }
  .talker {
    position: absolute; left: 0; top: 36px;
    width: 1200px; height: 600px;
    background: var(--white);
    overflow: hidden;
  }
  .adhesive-flap {
    position: absolute; left: 0; top: 0; width: 100%; height: 197px;
    background: var(--navy);
    border-bottom: 2px solid var(--navy-line);
  }
  .face-navy {
    position: absolute; left: 0; top: 199px; width: 100%; height: 246px;
    background: var(--navy);
  }
  .headline {
    position: absolute; left: 44px; top: 225px;
    color: var(--gold);
    font-weight: 900; font-size: 92px; line-height: 84px;
    letter-spacing: 1px; text-transform: uppercase;
  }
  .delivery-tag {
    position: absolute; left: 43px; top: 405px; width: 535px; height: 82px;
    background: var(--gold); color: var(--navy);
    font-weight: 900; font-size: 60px; line-height: 90px;
    text-align: center; text-transform: uppercase; letter-spacing: 1px;
  }
  .delivery-day {
    position: absolute; left: 0; top: 500px; width: 621px;
    color: var(--navy); text-align: center;
    font-weight: 900; font-size: 56px; line-height: 70px;
    text-transform: uppercase; letter-spacing: 1px;
  }
  .brand {
    position: absolute; left: 614px; top: 232px; width: 180px; height: 180px;
    border: 3px solid var(--gold); border-radius: 50%;
    display: flex; flex-direction: column; align-items: center; justify-content: center;
    color: var(--gold); font-weight: 800; text-transform: lowercase;
  }
  .brand-name { font-size: 46px; line-height: 42px; }
  .brand-sub { font-size: 22px; line-height: 26px; letter-spacing: 3px; }
  .claim-badges { position: absolute; left: 0; top: 0; width: 1200px; height: 600px; pointer-events: none; }
  .product-photo {
    position: absolute; left: 838px; top: 239px; width: 320px; height: 320px;
    border-radius: 50%; border: 10px solid var(--gold);
    background: radial-gradient(circle at 40% 45%, var(--tortilla-light) 0%, #e3cf9f 55%, var(--tortilla-dark) 100%);
  }
  .photo-ring { position: absolute; left: 0; top: 0; width: 1200px; height: 600px; pointer-events: none; }
</style>
</head>
<body>
  <main class="talker">
    <div class="adhesive-flap"></div>
    <div class="face-navy"></div>

    <h1 class="headline">Our Fresh<br>Tortillas</h1>
    <p class="delivery-tag">Are Delivered</p>
    <p class="delivery-day">Every...</p>

    <div class="brand">
      <span class="brand-name">lumo</span>
      <span class="brand-sub">flatbakes</span>
    </div>

    <svg class="claim-badges" viewBox="0 0 1200 600" aria-hidden="true">
      <g fill="var(--navy)" stroke="var(--gold)" stroke-width="3">
        <circle cx="633" cy="474" r="31"/>
        <circle cx="705" cy="474" r="31"/>
        <circle cx="775" cy="474" r="31"/>
        <circle cx="670" cy="543" r="31"/>
        <circle cx="741" cy="543" r="31"/>
      </g>
    </svg>

    <svg class="photo-ring" viewBox="0 0 1200 600" aria-hidden="true">
      <path d="M 880 237 A 191 191 0 1 1 900 563" fill="none" stroke="var(--gold)" stroke-width="2"/>
    </svg>
    <div class="product-photo" role="img" aria-label="Photo of a tall stack of fresh corn tortillas"></div>
  </main>
</body>
</html>
```